Plumbing business card and logo desgin

Need a new business card and logo for a plumbing business based in Warragul, Australia. Business name is 7Kelby plumbing & air-conditioning. We service all plumbing and gasfitting needs and installation of air-conditioning. We clear blocked drains, install new hot water systems, central heating, new and existing homes, roofing, sanitary and drainage.
i would like to have a space on there for website, email, phone, licence number and what we do as a company.
i would like a water droplet to be incorporated into the design to try and stand out that we are a plumbing business

Contact Information for Business Card

website:
phone number: 0458271936
Licence Number: 382716

Logo Text

Brenfield Plumbing & Air-Conditioning

```html
<!DOCTYPE html>
<html lang="en">
<head>
<meta charset="utf-8">
<title>Brenfield Plumbing &amp; Air-Conditioning – Business Card</title>
<link rel="stylesheet" href="https://fonts.googleapis.com/css2?family=Didact+Gothic&family=Montserrat:wght@600;700&display=swap">
<style>
  :root {
    --page: #e9e6e1;
    --card: #f2f3f5;
    --blue: #1277c4;
    --blue-light: #29a3e3;
    --blue-deep: #2a3fb0;
    --ink: #3a3a3c;
    --list-ink: #4a4a4d;
    --dark-band: #333336;
    --panel: rgba(150, 172, 218, 0.33);
    --strip: #f7f8fa;
  }
  * { box-sizing: border-box; margin: 0; padding: 0; }
  html, body { width: 1131px; height: 1200px; overflow: hidden; }
  body {
    background: var(--page);
    font-family: "Didact Gothic", "Century Gothic", sans-serif;
    color: var(--ink);
    position: relative;
  }
  .card {
    position: absolute;
    left: 178px;
    width: 776px;
    border-radius: 20px;
    background: var(--card);
    overflow: hidden;
    box-shadow: 0 10px 18px rgba(0,0,0,0.18);
  }
  .card--front { top: 103px; height: 445px; }
  .card--back { top: 614px; height: 443px; }

  .droplet-texture {
    position: absolute; inset: 0;
    background:
      radial-gradient(circle at 18% 25%, rgba(200,215,230,0.55), transparent 30%),
      radial-gradient(circle at 70% 20%, rgba(205,218,232,0.5), transparent 28%),
      radial-gradient(circle at 55% 75%, rgba(200,214,230,0.45), transparent 32%),
      radial-gradient(circle at 90% 70%, rgba(205,218,232,0.45), transparent 25%),
      var(--card);
  }

  /* front */
  .brand-mark {
    position: absolute; left: 60px; top: 208px; width: 280px; height: 60px;
    display: flex; align-items: center; justify-content: center; gap: 10px;
    font-family: "Montserrat", sans-serif; font-weight: 700;
    font-size: 40px; color: var(--blue-deep);
  }
  .brand-mark .dot { width: 22px; height: 22px; border-radius: 50%; background: var(--blue-deep); flex: none; }
  .divider {
    position: absolute; left: 392px; top: 138px; width: 2px; height: 182px;
    background: var(--blue);
  }
  .person { position: absolute; left: 463px; top: 128px; }
  .person__name { font-size: 32px; line-height: 38px; letter-spacing: 0.5px; }
  .person__name .initials { color: var(--blue); }
  .person__role { font-size: 16px; line-height: 20px; margin-top: 5px; letter-spacing: 0.5px; }
  .person__licence { font-size: 26px; line-height: 31px; color: var(--blue); margin-top: 9px; word-spacing: -2px; }
  .contact { position: absolute; left: 463px; top: 240px; list-style: none; }
  .contact li { display: flex; align-items: center; height: 27.5px; font-size: 18px; }
  .contact svg { width: 19px; height: 19px; margin-right: 14px; flex: none; }
  .contact .accent { color: var(--blue); }
  .front-band {
    position: absolute; left: 0; right: 0; bottom: 0; height: 18px;
    display: flex;
  }
  .front-band .blue { width: 401px; background: linear-gradient(90deg, var(--blue-light), var(--blue-deep)); }
  .front-band .dark { flex: 1; background: var(--dark-band); margin-left: 2px; }

  /* back */
  .logo-lockup {
    position: absolute; left: 186px; top: 46px;
    color: var(--blue); font-family: "Montserrat", sans-serif; font-weight: 600;
  }
  .logo-lockup .row { display: flex; align-items: center; gap: 12px; }
  .logo-lockup .dot { width: 30px; height: 30px; border-radius: 50%; background: var(--blue); flex: none; }
  .logo-lockup .name { font-size: 64px; line-height: 1; letter-spacing: 0.5px; }
  .logo-lockup .tagline { font-size: 21px; line-height: 26px; margin: 12px 0 0 96px; }
  .services-title {
    position: absolute; left: 106px; top: 189px; width: 582px; height: 59px;
    border-radius: 30px; background: var(--blue);
    color: #fff; font-family: "Montserrat", sans-serif; font-weight: 700;
    font-size: 36px; display: flex; align-items: center; justify-content: center;
  }
  .services-panel { position: absolute; inset: 0; }
  .service-list {
    position: absolute; top: 270px; list-style: none;
    font-size: 26px; color: var(--list-ink);
  }
  .service-list li { height: 33.5px; display: flex; align-items: center; white-space: nowrap; }
  .service-list li::before {
    content: ""; width: 14px; height: 14px; border-radius: 50%;
    background: var(--blue); margin-right: 12px; flex: none;
  }
  .service-list--left { left: 43px; }
  .service-list--right { left: 467px; }
  .back-band {
    position: absolute; left: 0; right: 0; bottom: 0; height: 38px;
    background: var(--blue);
  }
</style>
</head>
<body>

<section class="card card--front">
  <div class="droplet-texture" role="img" aria-label="Background of scattered clear water droplets"></div>
  <div class="brand-mark"><span class="dot"></span>Brenfield</div>
  <div class="divider"></div>
  <div class="person">
    <p class="person__name"><span class="initials">RT</span> MORENO</p>
    <p class="person__role">FOUNDER</p>
    <p class="person__licence">Licence No: 382716</p>
  </div>
  <ul class="contact">
    <li>
      <svg viewBox="0 0 20 20"><circle cx="10" cy="10" r="10" fill="#1277c4"/><path d="M7 5.5l2 2-1 1.3c.6 1.3 1.6 2.3 2.9 2.9l1.3-1 2 2-1.2 1.6c-3.5-.4-6.6-3.5-7-7z" fill="#fff"/></svg>
      0458271936
    </li>
    <li>
      <svg viewBox="0 0 20 20"><circle cx="10" cy="10" r="10" fill="#1277c4"/><rect x="5" y="6.5" width="10" height="7" fill="#fff"/><path d="M5 6.5l5 4 5-4" fill="none" stroke="#1277c4" stroke-width="1"/></svg>
      contact@brenfield.com.au
    </li>
    <li>
      <svg viewBox="0 0 20 20"><circle cx="10" cy="10" r="10" fill="#1277c4"/><circle cx="10" cy="10" r="5" fill="none" stroke="#fff" stroke-width="1.4"/><path d="M5 10h10M10 5c-2.5 3-2.5 7 0 10M10 5c2.5 3 2.5 7 0 10" fill="none" stroke="#fff" stroke-width="1"/></svg>
      <span>www.<span class="accent">brenfield</span>.com.au</span>
    </li>
  </ul>
  <div class="front-band"><span class="blue"></span><span class="dark"></span></div>
</section>

<section class="card card--back">
  <div class="droplet-texture" role="img" aria-label="Background of scattered clear water droplets"></div>
  <svg class="services-panel" viewBox="0 0 776 443" aria-hidden="true">
    <polygon points="383,272 776,272 776,389 150,389" fill="rgba(150,172,218,0.33)"/>
    <rect x="0" y="389" width="776" height="16" fill="#f7f8fa"/>
  </svg>
  <div class="logo-lockup">
    <div class="row"><span class="dot"></span><span class="name">Brenfield</span></div>
    <p class="tagline">Plumbing &amp; Air-Conditioning</p>
  </div>
  <h2 class="services-title">OUR SERVICE</h2>
  <ul class="service-list service-list--left">
    <li>installation of air-conditioning</li>
    <li>install new hot water systems</li>
    <li>plumbing and gasfitting</li>
    <li>new and existing homes</li>
  </ul>
  <ul class="service-list service-list--right">
    <li>sanitary and drainage</li>
    <li>clear blocked drains</li>
    <li>central heating</li>
    <li>roofing</li>
  </ul>
  <div class="back-band"></div>
</section>

</body>
</html>
```